Bluestone Advisory & Mgmt - Professional Business Cards

Hi!

I am a Real Estate Developer and Construction Consultant.

I have a lot of inspiration from previous designs and would be open to using the attached Designs as a starting point. I would like to see these styles incorporated into your designs.

I really need professional business card to go with it that includes my important info.

Look forward to seeing your designs!.

Target Market(s)

My Target market are building owners, lawyers, consultants.

Industry/Entity Type

Real Estate Development

Contact Information for Business Card

My Name: Dorian Pelkey
My Title: Principle
Company Name: Bluestone Advisory & Mgmt, LLC
Address: 348 West 71st Street, 9th FL New York, NY 10010
Mobile: 917.806.3971
Website: bam-hvx.example

Font styles to use
Serif
Sans Serif

Colors

Designer to choose colors to be used in the design.

Requirements
Must have
• Must incorporate the logo attached or have new that looks similar.
• Must use professional font that will be seen and judged by wealthy land owners and developers.
• Must incorporate some of the color green.
Should not have
• Photo's or pictures of people or buildings of any kind.

```html
<!DOCTYPE html>
<html lang="en">
<head>
<meta charset="utf-8">
<title>Bluestone Advisory &amp; Mgmt - Business Cards</title>
<link href="https://fonts.googleapis.com/css2?family=Montserrat:wght@300;400;700;800&display=swap" rel="stylesheet">
<style>
  :root {
    --backdrop: #2b2b2b;
    --brand-green: #4bb77b;
    --brand-green-soft: #5cc28a;
    --brand-grey: #8f8787;
    --text-grey: #7d7676;
    --card-white: #ffffff;
  }
  html, body {
    margin: 0;
    padding: 0;
    width: 1200px;
    height: 895px;
    overflow: hidden;
    background: var(--backdrop);
    font-family: "Montserrat", sans-serif;
  }
  .canvas {
    position: relative;
    width: 1200px;
    height: 895px;
  }
  .card {
    position: absolute;
    width: 660px;
    height: 377px;
    box-shadow: 0 18px 40px rgba(0,0,0,0.55);
    overflow: hidden;
  }
  /* Front */
  .card-front {
    left: 170px;
    top: 50px;
    background: var(--brand-green);
  }
  .front-map {
    position: absolute;
    left: 110px;
    top: 70px;
    width: 440px;
    height: 230px;
    border-radius: 50%;
    background: radial-gradient(ellipse at center, rgba(255,255,255,0.12), rgba(255,255,255,0) 70%);
  }
  .front-wordmark {
    position: absolute;
    left: 0;
    right: 0;
    top: 128px;
    text-align: center;
    color: var(--card-white);
    font-weight: 700;
    line-height: 1.05;
  }
  .front-wordmark .brand-main { display: block; font-size: 58px; letter-spacing: -1px; }
  .front-wordmark .brand-sub { display: block; font-size: 22px; letter-spacing: 1px; margin-top: 8px; }

  /* Back */
  .card-back {
    left: 370px;
    top: 468px;
    background: var(--card-white);
  }
  .back-stripe {
    position: absolute;
    left: 0;
    right: 0;
    bottom: 0;
    height: 10px;
    background: var(--brand-green);
  }
  .back-wordmark {
    position: absolute;
    left: 38px;
    top: 128px;
    width: 250px;
    color: var(--brand-green);
    font-weight: 700;
    line-height: 1.05;
  }
  .back-wordmark .brand-main { display: block; font-size: 44px; letter-spacing: -1px; }
  .back-wordmark .brand-sub { display: block; font-size: 17px; margin-top: 6px; }
  .divider {
    position: absolute;
    left: 300px;
    top: 70px;
    width: 1px;
    height: 230px;
    background: linear-gradient(to bottom, rgba(125,118,118,0), var(--text-grey) 30%, var(--text-grey) 70%, rgba(125,118,118,0));
  }
  .contact {
    position: absolute;
    left: 330px;
    top: 66px;
    width: 310px;
    color: var(--text-grey);
  }
  .person-name {
    margin: 0;
    font-size: 24px;
    font-weight: 800;
    letter-spacing: 0.5px;
    text-transform: uppercase;
  }
  .person-name .first { color: var(--brand-green); }
  .person-name .last { color: var(--brand-grey); }
  .person-title {
    margin: 2px 0 14px;
    font-size: 15px;
    font-weight: 400;
  }
  .address {
    margin: 0 0 14px;
    font-style: normal;
    font-size: 12.5px;
    line-height: 1.45;
  }
  .channels {
    list-style: none;
    margin: 0;
    padding: 0;
    font-size: 12.5px;
    line-height: 1.2;
  }
  .channels li {
    display: flex;
    align-items: center;
    gap: 10px;
    margin-bottom: 7px;
  }
  .channels svg {
    width: 14px;
    height: 14px;
    flex: none;
  }
</style>
</head>
<body>
<main class="canvas">
  <section class="card card-front" aria-label="Business card front">
    <div class="front-map" role="img" aria-label="Faint dotted world map in the background"></div>
    <div class="front-wordmark">
      <span class="brand-main">Bluestone</span>
      <span class="brand-sub">Advisory Management</span>
    </div>
  </section>

  <section class="card card-back" aria-label="Business card back">
    <div class="back-wordmark">
      <span class="brand-main">Bluestone</span>
      <span class="brand-sub">Advisory Management</span>
    </div>
    <div class="divider"></div>
    <div class="contact">
      <h1 class="person-name"><span class="first">Dorian</span> <span class="last">Pelkey</span></h1>
      <p class="person-title">Principle</p>
      <address class="address">
        Bluestone Advisory &amp; Mgmt, LLC<br>
        348 West 71st Street<br>
        9th FL New York, NY 10010
      </address>
      <ul class="channels">
        <li>
          <svg viewBox="0 0 24 24" aria-hidden="true"><path fill="#4bb77b" d="M6.6 10.8a15.1 15.1 0 0 0 6.6 6.6l2.2-2.2a1 1 0 0 1 1-.25 11.4 11.4 0 0 0 3.6.57 1 1 0 0 1 1 1V20a1 1 0 0 1-1 1A17 17 0 0 1 3 4a1 1 0 0 1 1-1h3.5a1 1 0 0 1 1 1c0 1.25.2 2.45.57 3.57a1 1 0 0 1-.25 1z"/></svg>
          917.806.3971
        </li>
        <li>
          <svg viewBox="0 0 24 24" aria-hidden="true"><rect x="3" y="5" width="18" height="14" fill="none" stroke="#4bb77b" stroke-width="2"/><path d="M3 6l9 7 9-7" fill="none" stroke="#4bb77b" stroke-width="2"/></svg>
          info@bam-hvx.example
        </li>
        <li>
          <svg viewBox="0 0 24 24" aria-hidden="true"><circle cx="12" cy="12" r="9" fill="none" stroke="#4bb77b" stroke-width="2"/><path d="M3 12h18M12 3c3 3 3 15 0 18M12 3c-3 3-3 15 0 18" fill="none" stroke="#4bb77b" stroke-width="1.6"/></svg>
          www.bam-hvx.example
        </li>
      </ul>
    </div>
    <div class="back-stripe"></div>
  </section>
</main>
</body>
</html>
```